Lawn mowing business card design

We need a business card design for our lawn mowing and gardening business which is located in the Northern Beaches of Sydney. Our business name is Meadowline Turf and our logo is predominantly green and yellow in color. Please see our website at www.meadowlineturf.com.au for design ideas. The business targets young professionals and older clientele. As such the font should be easy to read, but I also want the business card to be colorful and stand out.

Target Market(s)

young professionals

Industry/Entity Type

Lawn Care

Contact Information for Business Card

Meadowline Turf, Gareth Pellow, 0478559201, www.meadowlineturf.com.au, email: meadowlineturf@mailbox-example.com

Font styles to use
Serif

Colors
9bcb3b
fbed22

Requirements
Must have
• Must include the details listed above. Must include the attached logo.
Nice to have
• Logo attached with two copies. The logo without any writing is high quality, please feel free to be creative with the text stating our business name "Meadowline Turf" using this file.

```html
<!DOCTYPE html>
<html lang="en">
<head>
<meta charset="utf-8">
<title>Meadowline Turf – Business Card</title>
<link rel="stylesheet" href="https://fonts.googleapis.com/css2?family=PT+Sans:wght@400;700&display=swap">
<style>
  :root {
    --stage: #e9e6e0;
    --paper: #ffffff;
    --soil: #4a3e35;
    --soil-dark: #3b312a;
    --leaf: #8dc63f;
    --leaf-light: #a6d45a;
    --leaf-deep: #5ea62f;
    --meadow: #86c23c;
    --sun: #fbed22;
    --ink-light: #f4f1ec;
    --logo-green: #1f8a4c;
  }
  * { box-sizing: border-box; margin: 0; padding: 0; }
  html, body { width: 1200px; height: 950px; overflow: hidden; }
  body {
    background: var(--stage);
    font-family: "PT Sans", "Segoe UI", sans-serif;
    position: relative;
  }

  .card {
    position: absolute;
    overflow: hidden;
    border-radius: 4px;
    box-shadow: 0 10px 26px rgba(0,0,0,.22);
  }

  /* Front (portrait) */
  .card--front {
    left: 82px; top: 172px;
    width: 370px; height: 605px;
    background: var(--soil);
  }
  .front__top {
    position: absolute; inset: 0 0 auto 0;
    height: 300px;
    background: var(--paper);
  }
  .brand {
    position: absolute; left: 0; right: 0; top: 70px;
    display: flex; flex-direction: column; align-items: center; gap: 14px;
  }
  .brand__mark {
    width: 64px; height: 64px; border-radius: 50%;
    background: var(--sun);
  }
  .brand__name {
    font-size: 30px; font-weight: 700; color: var(--logo-green);
    letter-spacing: .5px;
  }
  .front__grass {
    position: absolute; left: 0; right: 0; top: 220px;
    height: 120px;
  }
  .front__details {
    position: absolute; left: 60px; right: 20px; top: 360px;
    color: var(--ink-light);
  }
  .person__name { font-size: 28px; font-weight: 700; color: var(--leaf); letter-spacing: .5px; }
  .person__role { font-size: 17px; margin-top: 4px; }
  .contact__phone { font-size: 25px; margin-top: 20px; letter-spacing: 1px; }
  .contact__line { font-size: 16px; margin-top: 6px; }
  .social { display: flex; gap: 9px; margin-top: 16px; }
  .social span { width: 20px; height: 20px; border-radius: 50%; background: var(--leaf); }

  /* Back (landscape) */
  .card--back {
    left: 512px; top: 290px;
    width: 605px; height: 370px;
    background: linear-gradient(160deg, var(--leaf-light), var(--meadow) 55%, var(--leaf-deep));
  }
  .back__mascot {
    position: absolute; right: 40px; top: 34px;
    width: 250px; height: 220px;
  }
  .back__grass {
    position: absolute; left: 0; right: 0; bottom: 104px;
    height: 70px;
  }
  .back__services {
    position: absolute; left: 0; right: 0; bottom: 0;
    height: 110px;
    background: var(--soil);
    color: var(--ink-light);
    padding: 18px 30px;
    font-size: 17px; line-height: 1.45;
  }
</style>
</head>
<body>

  <section class="card card--front" aria-label="Business card front">
    <div class="front__top"></div>
    <div class="brand">
      <span class="brand__mark"></span>
      <span class="brand__name">Meadowline Turf</span>
    </div>
    <svg class="front__grass" viewBox="0 0 370 120" preserveAspectRatio="none" role="img" aria-label="Band of green grass with small white daisies">
      <defs>
        <linearGradient id="frontGrass" x1="0" y1="0" x2="0" y2="1">
          <stop offset="0" stop-color="#a6d45a"/>
          <stop offset="1" stop-color="#5ea62f"/>
        </linearGradient>
      </defs>
      <path d="M0 40 Q90 30 185 60 T370 110 L370 120 L0 120 Z" fill="url(#frontGrass)"/>
      <path d="M0 95 Q120 85 230 105 T370 120 L0 120 Z" fill="#4a3e35"/>
    </svg>
    <div class="front__details">
      <p class="person__name">Gareth Pellow</p>
      <p class="person__role">CEO/Founder</p>
      <p class="contact__phone">0478559201</p>
      <p class="contact__line">meadowlineturf@mailbox-example.com</p>
      <p class="contact__line">www.meadowlineturf.com.au</p>
      <div class="social" aria-hidden="true">
        <span></span><span></span><span></span><span></span><span></span><span></span>
      </div>
    </div>
  </section>

  <section class="card card--back" aria-label="Business card back">
    <svg class="back__mascot" viewBox="0 0 250 220" role="img" aria-label="Mascot illustration area in yellow, grey and green">
      <defs>
        <linearGradient id="mascotTone" x1="0" y1="0" x2="1" y2="1">
          <stop offset="0" stop-color="#fbed22"/>
          <stop offset="1" stop-color="#2f8f4e"/>
        </linearGradient>
      </defs>
      <rect width="250" height="220" rx="10" fill="url(#mascotTone)" opacity=".55"/>
    </svg>
    <svg class="back__grass" viewBox="0 0 605 70" preserveAspectRatio="none" role="img" aria-label="Strip of grass blades">
      <path d="M0 30 Q150 10 300 30 T605 20 L605 70 L0 70 Z" fill="#5ea62f"/>
    </svg>
    <div class="back__services">
      <p>Lawn mowing | Edging | Blowing | Hedging</p>
      <p>Landscaping | Weeding | Poisoning | Mulching | Fertilising</p>
      <p>Rubbish removal | Planting Lawn care and advice | Turf</p>
    </div>
  </section>

</body>
</html>
```